Public School Stationary
Dravon ISD, The QUOLLS
Professional
Nora Tillings
Public Information Officer
415 Larkspur Ave.
Kelmont, TX 78921
nora.tillings@dravon.kyvel.net
www.dravon.kyvel.net
We need business cards and Letter Head for our School District. Because we are a school we want to display a very professional quality look and feel using our new logo.
We would like some ideas for the back of the card to really make our product stand out. I am thinking about using our logo just on the back.
Primary Logo

```html
<!DOCTYPE html>
<html lang="en">
<head>
<meta charset="utf-8">
<title>Dravon ISD Stationery</title>
<link href="https://fonts.googleapis.com/css2?family=Open+Sans:wght@400;600;700&display=swap" rel="stylesheet">
<style>
:root{
  --backdrop:#5b5d60;
  --paper:#ffffff;
  --ink:#333333;
  --muted:#777777;
  --orange:#e8702a;
  --orange-deep:#c9561a;
  --gray:#8a8c8f;
  --gray-dark:#4a4c4f;
  --rule:#b5b5b5;
}
*{box-sizing:border-box;margin:0;padding:0}
html,body{width:1200px;height:557px;overflow:hidden}
body{background:var(--backdrop);font-family:"Open Sans",Arial,sans-serif;color:var(--ink);position:relative}
.sheet,.envelope,.card{position:absolute;background:var(--paper);box-shadow:0 2px 6px rgba(0,0,0,.35);overflow:hidden}
.wave{position:absolute;left:0;bottom:0;width:100%}
.brand{position:absolute;display:flex;flex-direction:column;align-items:center;gap:2px}
.brand-mark{width:18px;height:18px;border-radius:50%;background:var(--orange)}
.brand-name{font-weight:700;color:var(--orange);font-size:7px;line-height:1.1;text-align:center}
.contact{position:absolute;font-size:4.6px;line-height:1.45;color:var(--muted)}
.contact .name{font-weight:700;color:var(--ink);font-size:5.6px}

/* letterhead */
.letterhead{left:72px;top:72px;width:324px;height:451px}
.letterhead .brand{left:22px;top:18px}
.letterhead .contact{left:226px;top:18px}

/* fax */
.fax{left:420px;top:72px;width:324px;height:451px}
.fax .brand{left:22px;top:18px}
.fax .contact{left:226px;top:18px}
.fax-title{position:absolute;left:22px;top:96px;font-size:20px;font-weight:400;letter-spacing:.5px}
.fax-fields{position:absolute;left:22px;top:128px;width:280px;display:grid;grid-template-columns:1fr 1fr;column-gap:16px;row-gap:9px}
.fax-field{display:flex;align-items:flex-end;gap:4px;font-size:4.6px;color:var(--muted)}
.fax-field span.line{flex:1;border-bottom:.6px solid var(--rule);height:6px}
.fax-checks{position:absolute;left:22px;top:200px;width:280px;display:flex;justify-content:space-between;font-size:4.4px;color:var(--muted)}
.fax-checks span{display:flex;align-items:center;gap:3px}
.fax-checks i{display:inline-block;width:6px;height:6px;border:.6px solid var(--gray)}

/* envelopes */
.envelope-back{left:749px;top:79px;width:379px;height:180px}
.envelope-back .flap{position:absolute;left:0;top:0;width:100%;height:100%}
.envelope-back .brand{left:50%;top:14px;transform:translateX(-50%)}
.envelope-front{left:768px;top:211px;width:372px;height:149px}
.envelope-front .brand{left:16px;top:12px}
.envelope-front .contact{left:60px;top:12px}

/* cards */
.card{width:120px;height:60px}
.card-front-a{left:900px;top:379px}
.card-front-b{left:1032px;top:379px}
.card-back-a{left:900px;top:451px}
.card-back-b{left:1032px;top:451px}
.card .brand{left:10px;top:8px}
.card .brand-mark{width:12px;height:12px}
.card .brand-name{font-size:5px}
.card .contact{left:52px;top:7px;font-size:3.6px}
.card .contact .name{font-size:4.6px}
.card-back{background:linear-gradient(160deg,#f2f2f2,#cfd0d2)}
.card-back .brand{left:8px;top:8px;flex-direction:row;gap:4px}
.card-back .brand-name{text-align:left}
.card-back .back-url{position:absolute;left:8px;top:26px;font-size:3.8px;color:var(--gray-dark)}
</style>
</head>
<body>

<svg width="0" height="0" style="position:absolute">
  <defs>
    <linearGradient id="swoosh-gray" x1="0" y1="0" x2="1" y2="0">
      <stop offset="0" stop-color="#6e7073"/>
      <stop offset="1" stop-color="#a9abad"/>
    </linearGradient>
  </defs>
</svg>

<section class="sheet letterhead">
  <div class="brand"><span class="brand-mark"></span><span class="brand-name">Dravon ISD<br>The QUOLLS</span></div>
  <div class="contact">
    <div class="name">Nora Tillings</div>
    Public Information Officer<br>415 Larkspur Ave.<br>Kelmont, TX 78921<br>(512) 555-0148<br>nora.tillings@dravon.kyvel.net<br>www.dravon.kyvel.net
  </div>
  <svg class="wave" viewBox="0 0 100 20" height="64" preserveAspectRatio="none">
    <path d="M0 9 C30 22 60 -1 100 5 L100 20 L0 20Z" fill="url(#swoosh-gray)"/>
    <path d="M0 6 C30 19 60 -3 100 2" fill="none" stroke="var(--orange)" stroke-width="1.4"/>
  </svg>
</section>

<section class="sheet fax">
  <div class="brand"><span class="brand-mark"></span><span class="brand-name">Dravon ISD<br>The QUOLLS</span></div>
  <div class="contact">
    <div class="name">Nora Tillings</div>
    Public Information Officer<br>415 Larkspur Ave.<br>Kelmont, TX 78921<br>(512) 555-0148<br>nora.tillings@dravon.kyvel.net<br>www.dravon.kyvel.net
  </div>
  <h1 class="fax-title">FAX</h1>
  <div class="fax-fields">
    <div class="fax-field">To<span class="line"></span></div>
    <div class="fax-field">From<span class="line"></span></div>
    <div class="fax-field">Fax<span class="line"></span></div>
    <div class="fax-field">Pages<span class="line"></span></div>
    <div class="fax-field">Phone<span class="line"></span></div>
    <div class="fax-field">Date<span class="line"></span></div>
    <div class="fax-field">Re<span class="line"></span></div>
    <div class="fax-field">CC<span class="line"></span></div>
  </div>
  <div class="fax-checks">
    <span><i></i>Urgent</span><span><i></i>For Review</span><span><i></i>Please Comment</span><span><i></i>Please Reply</span><span><i></i>Please Recycle</span>
  </div>
  <svg class="wave" viewBox="0 0 100 20" height="64" preserveAspectRatio="none">
    <path d="M0 9 C30 22 60 -1 100 5 L100 20 L0 20Z" fill="url(#swoosh-gray)"/>
    <path d="M0 6 C30 19 60 -3 100 2" fill="none" stroke="var(--orange)" stroke-width="1.4"/>
  </svg>
</section>

<section class="envelope envelope-back">
  <svg class="flap" viewBox="0 0 379 180" preserveAspectRatio="none">
    <path d="M0 0 L189.5 70 L379 0" fill="none" stroke="#d6d6d6" stroke-width="1"/>
  </svg>
  <div class="brand"><span class="brand-mark"></span><span class="brand-name">Dravon ISD</span></div>
</section>

<section class="envelope envelope-front">
  <div class="brand"><span class="brand-mark"></span><span class="brand-name">Dravon ISD</span></div>
  <div class="contact">
    <div class="name">Nora Tillings</div>
    415 Larkspur Ave.<br>Kelmont, TX 78921<br>www.dravon.kyvel.net
  </div>
  <svg class="wave" viewBox="0 0 100 20" height="26" preserveAspectRatio="none">
    <path d="M0 9 C30 22 60 -1 100 5 L100 20 L0 20Z" fill="url(#swoosh-gray)"/>
    <path d="M0 6 C30 19 60 -3 100 2" fill="none" stroke="var(--orange)" stroke-width="1.4"/>
  </svg>
</section>

<section class="card card-front-a">
  <div class="brand"><span class="brand-mark"></span><span class="brand-name">Dravon ISD</span></div>
  <div class="contact"><div class="name">Nora Tillings</div>Public Information Officer<br>(512) 555-0148<br>nora.tillings@dravon.kyvel.net</div>
  <svg class="wave" viewBox="0 0 100 20" height="14" preserveAspectRatio="none">
    <path d="M0 9 C30 22 60 -1 100 5 L100 20 L0 20Z" fill="url(#swoosh-gray)"/>
    <path d="M0 6 C30 19 60 -3 100 2" fill="none" stroke="var(--orange)" stroke-width="1.6"/>
  </svg>
</section>

<section class="card card-front-b">
  <div class="brand"><span class="brand-mark"></span><span class="brand-name">Dravon ISD</span></div>
  <div class="contact"><div class="name">Nora Tillings</div>Public Information Officer<br>(512) 555-0148<br>nora.tillings@dravon.kyvel.net</div>
  <svg class="wave" viewBox="0 0 100 20" height="14" preserveAspectRatio="none">
    <path d="M0 9 C30 22 60 -1 100 5 L100 20 L0 20Z" fill="url(#swoosh-gray)"/>
    <path d="M0 6 C30 19 60 -3 100 2" fill="none" stroke="var(--orange)" stroke-width="1.6"/>
  </svg>
</section>

<section class="card card-back card-back-a">
  <div class="brand"><span class="brand-mark"></span><span class="brand-name">Dravon ISD<br>The QUOLLS</span></div>
  <div class="back-url">www.dravon.kyvel.net</div>
  <svg class="wave" viewBox="0 0 100 20" height="16" preserveAspectRatio="none">
    <path d="M0 9 C30 22 60 -1 100 5 L100 20 L0 20Z" fill="var(--gray-dark)"/>
    <path d="M0 6 C30 19 60 -3 100 2" fill="none" stroke="var(--orange)" stroke-width="1.6"/>
  </svg>
</section>

<section class="card card-back card-back-b">
  <div class="brand"><span class="brand-mark"></span><span class="brand-name">Dravon ISD<br>The QUOLLS</span></div>
  <div class="back-url">www.dravon.kyvel.net</div>
  <svg class="wave" viewBox="0 0 100 20" height="16" preserveAspectRatio="none">
    <path d="M0 9 C30 22 60 -1 100 5 L100 20 L0 20Z" fill="var(--gray-dark)"/>
    <path d="M0 6 C30 19 60 -3 100 2" fill="none" stroke="var(--orange)" stroke-width="1.6"/>
  </svg>
</section>

</body>
</html>
```